Responsive WordPress website for medical therapy practice consulting business.

We need both design and website for responsive Wordpress website. The use of Tessaly theme is preferred when considering the design (not required).
Site must be designed for 1920px width and fully responsive.
See full scope of the project below.

DESIGN:
Design a full screen layout using images and parallax movement where appropriate.
Easy to use navigation for desktop and hamburger style navigation for mobile devices.
Create an original design for the home, sub-page template.
Create a responsive website using common desktop breakpoints 1920, 1366, 1280 1024 as well as mobile devices.
Color scheme should use soft or pastel color avoiding reds.
Design will take inspiration from logo design and color scheme.
Large “Hero slider” may be employed to striking visual interest.
The website will focus the content on the Homepage mission statement, What We Do and How to Reach Us, content.
Website Footer Information: Include content for Privacy Policy and Terms of Use, address and copyright information.

DEVELOPMENT NOTES:

WordPress content management platform will be used .

Responsive grid will be used to properly display website content on all devices including mobile, laptop and desktop at standard breakpoints.

Social Media links to LinkedIn and Twitter

Google Analytics and Search Console integration – allows tracking of visitors and in-depth search data, indexing and performance.

Yoast Basic SEO – basic setup and integration is included in the proposal. This includes creating SEO friendly page titles, search descriptions and best practices for heading and image tags.

508 & ADA compliance

PAGE LIST:
The following pages are a list of current websites pages. These are used as a guideline for developing the proposal and can be changed to reflect content:

NAVIGATION LINKS:

HOME

· Featuring the new logo, the home page will display Brenlow Care Advisor’s message, services, and contact information.
· The navigation will be prominent, intuitive and easy to use, allowing to find information quickly.
· Parallax scrolling will provide a cool modern visual effect without being overbearing.

====================================================

ABOUT US –

· History
· Bios
· Links

SERVICES

· Business Consultancy service

CONTACT US – This section will present ways for viewers to reach out either by phone, email.

· Google map of office locations.
· Business information
a. Locations
b. Address
c. Phone
d. Fax
e. Email

FOOTER LINKS – Additional information for legal or usage claims, company info and contact info.

· Copyright information
· Links to CONTACT
· Social Media
· Disclaimer
· Privacy policy
· Terms of use

```html
<!DOCTYPE html>
<html lang="en">
<head>
<meta charset="utf-8">
<title>Brenlow Care Advisors — Home</title>
<link rel="stylesheet" href="https://fonts.googleapis.com/css2?family=Questrial&display=swap">
<style>
  :root {
    --blue-deep: #1d56a6;
    --blue-mid: #1f67b8;
    --blue-light: #1b86d2;
    --white: #ffffff;
    --white-soft: rgba(255,255,255,0.88);
    --menu-text: #2a3a55;
    --menu-active: #1b8fdc;
  }
  * { margin: 0; padding: 0; box-sizing: border-box; }
  html, body { width: 1200px; height: 626px; overflow: hidden; }
  body { font-family: "Questrial", "Century Gothic", sans-serif; color: var(--white); background: var(--blue-mid); }

  .hero { position: relative; width: 1200px; height: 626px; overflow: hidden; }
  .hero__photo {
    position: absolute; inset: 0;
    background:
      radial-gradient(ellipse 260px 320px at 700px 260px, rgba(255,255,255,0.07), transparent 70%),
      linear-gradient(180deg, var(--blue-deep) 0%, var(--blue-mid) 55%, var(--blue-light) 100%);
  }

  .site-header { position: relative; z-index: 2; text-align: center; padding-top: 34px; }
  .brand { display: inline-flex; align-items: center; gap: 10px; font-size: 22px; letter-spacing: 0.5px; color: var(--white); }
  .brand__mark { width: 12px; height: 12px; border-radius: 50%; background: var(--white); }

  .main-nav { margin-top: 30px; display: flex; justify-content: center; gap: 32px; }
  .main-nav__item { position: relative; font-size: 11px; letter-spacing: 0.6px; text-transform: uppercase; }
  .main-nav__item--current::after {
    content: ""; position: absolute; left: 0; right: 0; bottom: -6px; height: 1px; background: var(--white);
  }
  .submenu {
    position: absolute; top: 20px; left: 0; width: 86px;
    background: var(--white); list-style: none; padding-bottom: 6px;
    box-shadow: 0 2px 6px rgba(0,0,0,0.25);
    border-top: 3px solid var(--menu-active);
  }
  .submenu li { font-size: 10px; color: var(--menu-text); padding: 4px 8px 2px; text-align: left; }
  .submenu .submenu__item--active { background: var(--menu-active); color: var(--white); padding-bottom: 4px; }
  .pointer { position: absolute; right: 14px; top: 6px; }

  .hero__content { position: relative; z-index: 2; text-align: center; margin-top: 170px; }
  .hero__title { font-weight: 400; font-size: 26px; line-height: 34px; letter-spacing: 0.4px; text-transform: uppercase; }
  .hero__text { width: 560px; margin: 16px auto 0; font-size: 12.5px; line-height: 16px; color: var(--white-soft); }
  .hero__button {
    display: inline-block; margin-top: 30px; width: 188px; height: 40px; line-height: 40px;
    background: var(--white); color: var(--blue-mid); font-size: 16px; text-decoration: none;
  }
</style>
</head>
<body>
  <section class="hero">
    <div class="hero__photo" role="img" aria-label="Blue-toned photo of a therapist consulting with a client in an office"></div>

    <header class="site-header">
      <div class="brand"><span class="brand__mark"></span>Brenlow Care Advisors</div>
      <nav class="main-nav">
        <span class="main-nav__item main-nav__item--current">Home</span>
        <span class="main-nav__item">About Us
          <ul class="submenu">
            <li class="submenu__item--active">History
              <svg class="pointer" width="10" height="12" viewBox="0 0 10 12" aria-hidden="true"><path d="M2 1v8l2-2 2 4 1.5-.7-2-4H8z" fill="#fff" stroke="#222" stroke-width="0.8"/></svg>
            </li>
            <li>Bios</li>
            <li>Links</li>
          </ul>
        </span>
        <span class="main-nav__item">Services</span>
        <span class="main-nav__item">Contact Us</span>
      </nav>
    </header>

    <div class="hero__content">
      <h1 class="hero__title">Lorem ipsum dolor sit amet,<br>consectetur adipiscing elit, sed</h1>
      <p class="hero__text">Lorem ipsum dolor sit amet, consectetur adipiscing elit, sed do eiusmod tempor incididunt ut labore et dolore magna aliqua. Quis ipsum suspendisse ultrices gravida. Risus commodo viverra maecenas accumsan lacus vel facilisis.</p>
      <a class="hero__button" href="#contact">Contact Now</a>
    </div>
  </section>
</body>
</html>
```